Design a Professional Business Card for Velmora Arcs

Design a business card for Velmora Arcs, we are a National Sport Court Company.

West Region Address: 4175 Quill Harbor Ln, Suite #215 Ashcombe, Montana 80467
East Region Address: 3817 Tamsin Rd E, Bradenton, Florida 34583

Target Market(s)

High End Residential & Institutional Clients

Industry/Entity Type

Design & Construction

Contact Information for Business Card

Logo/Brand/Colors/ name, number (provided in comments)

Requirements
Must have
• Colors only provided in logo
Should not have
• Any other colors not in existing logo (attached)

```html
<!DOCTYPE html>
<html lang="en">
<head>
<meta charset="utf-8">
<title>Velmora Arcs — Business Card</title>
<link rel="stylesheet" href="https://fonts.googleapis.com/css2?family=Montserrat:wght@400;500;700&display=swap">
<style>
  :root {
    --navy: #1b3468;
    --green: #136b35;
    --white: #ffffff;
    --mist: #e9e9ee;
    --backdrop: #6b5646;
  }
  * { margin: 0; padding: 0; box-sizing: border-box; }
  html, body {
    width: 956px; height: 1200px; overflow: hidden;
    background: var(--backdrop);
    font-family: "Montserrat", sans-serif;
  }
  .canvas { position: relative; width: 956px; height: 1200px; }

  .card {
    position: absolute; left: 203px; width: 539px; height: 308px; overflow: hidden;
  }
  .card-front { top: 253px; background: var(--white); }
  .card-back {
    top: 650px;
    background: radial-gradient(ellipse 60% 70% at 50% 55%, #176b3e 0%, #125654 45%, var(--navy) 100%);
  }

  .brand { position: absolute; display: flex; align-items: center; }
  .brand-mark { border-radius: 50%; flex: none; }
  .brand-name {
    font-weight: 700; line-height: 0.95; letter-spacing: 0.06em; text-transform: uppercase;
  }
  .card-front .brand { right: 30px; top: 34px; gap: 14px; }
  .card-front .brand-mark { width: 70px; height: 70px; background: var(--navy); }
  .card-front .brand-name { color: var(--navy); font-size: 29px; }
  .card-back .brand { left: 107px; top: 108px; gap: 18px; }
  .card-back .brand-mark { width: 90px; height: 90px; background: var(--mist); }
  .card-back .brand-name { color: var(--mist); font-size: 37px; }

  .person { position: absolute; left: 32px; top: 148px; color: var(--navy); }
  .person-name { font-weight: 700; font-size: 22px; line-height: 1.1; }
  .person-title { font-weight: 500; font-size: 14px; margin-top: 2px; }

  .divider {
    position: absolute; left: 32px; right: 30px; top: 199px; height: 2px; background: var(--green);
  }

  .contacts {
    position: absolute; left: 32px; top: 212px; list-style: none;
    color: var(--navy); font-size: 13px; font-weight: 500; line-height: 19px;
  }
  .contacts li { display: flex; align-items: center; gap: 8px; }
  .contacts svg { width: 12px; height: 12px; flex: none; fill: var(--green); }

  .office {
    position: absolute; right: 30px; top: 212px; text-align: right;
    color: var(--navy); font-size: 13px; font-weight: 500; line-height: 19px;
  }
  .office-region { color: var(--green); font-weight: 700; }

  .footer-bands { position: absolute; left: 0; bottom: 0; width: 539px; height: 30px; }
</style>
</head>
<body>
<main class="canvas">

  <section class="card card-front" aria-label="Business card front">
    <div class="brand">
      <span class="brand-mark"></span>
      <span class="brand-name">Velmora<br>Arcs</span>
    </div>

    <div class="person">
      <p class="person-name">Darin Holloway</p>
      <p class="person-title">Director</p>
    </div>

    <div class="divider"></div>

    <ul class="contacts">
      <li>
        <svg viewBox="0 0 12 12"><path d="M3 0h6a1 1 0 0 1 1 1v10a1 1 0 0 1-1 1H3a1 1 0 0 1-1-1V1a1 1 0 0 1 1-1zm.5 1.5v8h5v-8zM6 10.2a.6.6 0 1 0 0 1.2.6.6 0 0 0 0-1.2z"/></svg>
        1-555-308214
      </li>
      <li>
        <svg viewBox="0 0 12 12"><path d="M0 2.5h12v7H0zM1 3.3l5 3.4 5-3.4v-.1H1zM1 4.4v4.3l3-2.2zm10 0L8 6.5l3 2.2z"/></svg>
        darin@velmoraarcs.com
      </li>
      <li>
        <svg viewBox="0 0 12 12"><circle cx="6" cy="6" r="6"/><path d="M3 3.5c1 0 1.5.7 2.3.5.6.8-.3 1.4.2 2.2.6.6 1.2 1.1.7 2.2-.8.3-1.6-.6-1.8-1.6C4 6.3 2.7 6 2.4 5 2.3 4.3 2.5 3.8 3 3.5zM7.8 2.4c.9.2 1.8.9 2.1 2-.7 0-1.2-.3-1.5-.9-.4-.3-.7-.6-.6-1.1z" fill="#fff"/></svg>
        www.velmoraarcs.com
      </li>
    </ul>

    <div class="office">
      <p class="office-region">West Region</p>
      <p>4175 Quill Harbor Ln</p>
      <p>Suite #215 Ashcombe, Montana 80467</p>
    </div>

    <svg class="footer-bands" viewBox="0 0 539 30" preserveAspectRatio="none" aria-hidden="true">
      <rect x="0" y="11" width="285" height="19" fill="var(--green)"/>
      <polygon points="268,30 297,0 539,0 539,30" fill="var(--white)"/>
      <polygon points="271,30 298,0 539,0 539,30" fill="var(--navy)"/>
    </svg>
  </section>

  <section class="card card-back" aria-label="Business card back">
    <div class="brand">
      <span class="brand-mark"></span>
      <span class="brand-name">Velmora<br>Arcs</span>
    </div>
  </section>

</main>
</body>
</html>
```